Selkirk Boat Lines and Freight Business Card

I need business cards for my new water taxi and freight transport business I have started here in Kodiak Alaska. Kodiak is a remote island in the middle of the gulf of Alaska. There are seven native villages around the island and Kodiak is the #2 fishing port in the United States. We also have the largest Seaward Corps Base in the U.S. My company will be providing water taxi and freight transport logistics to the villages and many hunting and fishing lodges as well as remote properties around the island.

I would like a business card that isn't status quo, something that stands out, either in feel or appearance. I do like clean minimal designs but it needs to have the necessary contact info on it.

Target Market(s)

remote lodge / property owners, residents of the many villages around Kodiak and any one wanting to enjoy the great outdoors of Kodiak Alaska

Industry/Entity Type

Business

Contact Information for Business Card

I like clean simple designs that aren't cluttered but still provide the necessary information

Colors
0255a3
3277b5
33a4d5
9bcb3c
add136
fbed22
ffc214
f78f20
f37122

Requirements
Must have
• logo and contact info
• Captain Marcus Hollend
• www.selkirkboatlines.com
• marcus@selkirkboatlines.com

```html
<!DOCTYPE html>
<html lang="en">
<head>
<meta charset="utf-8">
<title>Selkirk Boat Lines and Freight – Business Card</title>
<link rel="stylesheet" href="https://fonts.googleapis.com/css2?family=Open+Sans:wght@400;600;700;800&display=swap">
<style>
  :root {
    --page: #e9ebee;
    --white: #ffffff;
    --navy: #0a3f8f;
    --blue: #0255a3;
    --mid-blue: #3277b5;
    --sky: #33a4d5;
    --orange: #f78f20;
    --olive: #4a4a2c;
    --text-light: #e6f1fb;
  }
  * { box-sizing: border-box; margin: 0; padding: 0; }
  html, body {
    width: 1200px; height: 913px; overflow: hidden;
    background: var(--page);
    font-family: "Open Sans", Arial, sans-serif;
  }
  .sheet {
    position: relative; width: 1200px; height: 913px;
    display: flex; align-items: center; justify-content: center; gap: 40px;
  }
  .card {
    position: relative; width: 540px; height: 309px;
    border-radius: 18px; overflow: hidden;
    box-shadow: 0 10px 26px rgba(0, 30, 70, 0.22);
  }
  .card-front { background: var(--white); }
  .front-wave { position: absolute; inset: 0; width: 100%; height: 100%; }

  .brand {
    position: absolute; left: 30px; top: 100px; width: 220px;
    display: flex; align-items: center; gap: 10px;
  }
  .brand-dot {
    width: 26px; height: 26px; border-radius: 50%;
    background: var(--orange); flex: none;
  }
  .brand-name {
    color: var(--blue); font-weight: 800; font-size: 19px;
    line-height: 1.2; letter-spacing: 0.1px;
  }

  .contact {
    position: absolute; right: 24px; top: 122px; width: 220px;
    text-align: right; color: var(--white);
  }
  .contact-name { font-weight: 700; font-size: 17px; margin-bottom: 6px; white-space: nowrap; }
  .contact-line {
    display: flex; justify-content: flex-end; align-items: center; gap: 7px;
    font-size: 12px; color: var(--text-light); line-height: 1.55; white-space: nowrap;
  }
  .contact-icon { width: 11px; height: 11px; flex: none; }

  .card-back {
    background: radial-gradient(ellipse at 50% 35%, var(--mid-blue) 0%, var(--blue) 55%, var(--navy) 100%);
    display: flex; align-items: center; justify-content: center;
  }
  .back-brand { display: flex; align-items: center; gap: 14px; }
  .back-brand .brand-dot { width: 30px; height: 30px; }
  .back-brand .brand-name { color: var(--white); font-size: 26px; }
</style>
</head>
<body>
<main class="sheet">

  <section class="card card-front">
    <svg class="front-wave" viewBox="0 0 540 309" preserveAspectRatio="none" aria-hidden="true">
      <defs>
        <linearGradient id="waveBlue" x1="0" y1="0" x2="0" y2="1">
          <stop offset="0" stop-color="#3277b5"/>
          <stop offset="1" stop-color="#0a3f8f"/>
        </linearGradient>
        <path id="waveShape" d="M0,250 C130,300 210,220 280,140 S440,50 540,55 L540,309 L0,309 Z"/>
      </defs>
      <use href="#waveShape" transform="translate(0,-20)" fill="var(--olive)"/>
      <use href="#waveShape" transform="translate(0,-17)" fill="var(--white)"/>
      <use href="#waveShape" transform="translate(0,-14)" fill="var(--orange)"/>
      <use href="#waveShape" transform="translate(0,-9)" fill="var(--white)"/>
      <use href="#waveShape" transform="translate(0,-6)" fill="var(--sky)"/>
      <use href="#waveShape" fill="url(#waveBlue)"/>
    </svg>

    <div class="brand">
      <span class="brand-dot"></span>
      <div class="brand-name">Selkirk Boat Lines<br>and Freight</div>
    </div>

    <div class="contact">
      <div class="contact-name">Captain Marcus Hollend</div>
      <div class="contact-line">
        <span>marcus@selkirkboatlines.com</span>
        <svg class="contact-icon" viewBox="0 0 12 12" aria-hidden="true">
          <rect x="0.5" y="2" width="11" height="8" rx="1" fill="var(--orange)"/>
          <path d="M1,2.5 L6,6.5 L11,2.5" fill="none" stroke="#fff" stroke-width="1"/>
        </svg>
      </div>
      <div class="contact-line">
        <span>www.selkirkboatlines.com</span>
        <svg class="contact-icon" viewBox="0 0 12 12" aria-hidden="true">
          <circle cx="6" cy="6" r="5.2" fill="var(--orange)"/>
          <path d="M1,6 H11 M6,1 V11 M3,2.8 Q6,4.5 9,2.8 M3,9.2 Q6,7.5 9,9.2" fill="none" stroke="#fff" stroke-width="0.8"/>
        </svg>
      </div>
    </div>
  </section>

  <section class="card card-back">
    <div class="back-brand">
      <span class="brand-dot"></span>
      <div class="brand-name">Selkirk Boat Lines<br>and Freight</div>
    </div>
  </section>

</main>
</body>
</html>
```